Flyer for Student Management Consulting wanted - take a break!

"VENDA Consulting eV" is the student management consultancy of the Halvering Academy of Applied Studies. We are looking for a flyer to be printed on both sides. Students are to be advertised on one page. On the other side of the flyer, companies are to be approached, where we would like to offer consulting services. Both sides should stand out from each other on the basis of the various target groups, but be coherent in themselves. The front (for students) can be designed "hip" and creative - and the backside (for companies) simply and timelessly designed. There are no limits to the creativity - work with pictures, icons, etc. If you like, you can also get inspiration on the new website: https://mail502913.pagebuilder-example.com/venda Please note the following: Name Of the association: VENDA Consulting eV Color code: RGB: 3A4D98 Font: Simple and timeless Please use the attached logo The flyer should have the following content: Front: For students - exchange - experience - community path from the books to the practice. Become part of a dynamic team and shape your future with us. Contact: VENDA Consulting eV Student Advisory Service Brunnwieser Allee 37-41 26073 Oldenburg E-Mail: kontakt@venda-beratung.example Web: www.venda-beratung.example Facebook: VENDA Consulting eV - Network - Fresh ideas - Flexible operation Are you looking for external support for targeted problem solving? We offer your company a young and dynamic team of different disciplines, with only one focus: the added value! Contact: VENDA Consulting eV Student Management Consultancy Brunnwieser Allee 37-41 26073 Oldenburg Email: kontakt@venda-beratung.example Web: www.venda-beratung.example Facebook: VENDA Consulting eV - Student Consulting

Target Market(s)

Students are to be advertised on one page. On the other side of the flyer, companies are to be approached, where we would like to offer consulting services. Both sides should stand out from each other on the basis of the various target groups, but be coherent in themselves.

Industry/Entity Type

Consulting

Font styles to use
Serif

Colors
0255a3

Requirements
Must have
• Please note the following: The name of the association: VENDA Consulting eV Color code: RGB: 3A4D98 Font: Plain and timeless Please use the attached logo The flyer should have the following contents: Front: For students - exchange - experience - community path from the books , Go to the practice. Become part of a dynamic team and shape your future with us. Contact: VENDA Consulting eV Student Advisory Service Brunnwieser Allee 37-41 26073 Oldenburg E-Mail: kontakt@venda-beratung.example Web: www.venda-beratung.example Facebook: VENDA Consulting eV - The student company consulting Back: For companies - Large network - Fresh ideas - Flexible working method Are you looking for external support for goal-oriented problem solving? We offer your company a young and dynamic team of different disciplines, with only one focus: the added value! Contact: VENDA Consulting eV Student Advisory Service Brunnwieser Allee 37-41 26073 Oldenburg E-Mail: kontakt@venda-beratung.example Web: www.venda-beratung.example Facebook: VENDA Consulting eV - Student Consulting
Nice to have
• Images, icons, graphics etc.
Should not have
• Ornate writing

```html
<!DOCTYPE html>
<html lang="de">
<head>
<meta charset="utf-8">
<title>VENDA Consulting e.V. – Flyer Vorder- und Rückseite</title>
<link rel="stylesheet" href="https://fonts.googleapis.com/css2?family=Lato:wght@400;700;900&family=Roboto+Condensed:wght@300;400;700&display=swap">
<style>
  :root{
    --brand:#3a4d98;
    --brand-bright:#4656ad;
    --ink:#2b2b2d;
    --grey-text:#6d6d70;
    --dark:#3e3e40;
    --dark-2:#4b4b4d;
    --light:#ececed;
    --paper:#ffffff;
    --stage:#2a211c;
  }
  *{box-sizing:border-box;margin:0;padding:0}
  html,body{width:1200px;height:1200px;overflow:hidden;background:var(--stage)}
  .canvas{position:relative;width:1200px;height:1200px}
  .flyer{position:absolute;width:558px;height:782px;background:var(--paper);
    transform:scale(.96);transform-origin:0 0;overflow:hidden;
    box-shadow:0 10px 30px rgba(0,0,0,.5);font-family:"Lato",sans-serif}
  .flyer--front{left:40px;top:224px}
  .flyer--back{left:624px;top:224px}
  .abs{position:absolute}

  /* brand mark */
  .brand{position:absolute;display:flex;align-items:flex-start;gap:8px}
  .brand__name{font-family:"Lato",sans-serif;font-weight:400;font-size:40px;letter-spacing:4px;color:#111;line-height:1}
  .brand__sub{font-size:6px;line-height:1.25;color:#222;white-space:nowrap}
  .brand__sub b{font-weight:700}

  /* front */
  .front-rule{left:0;top:3px;width:100%;height:4px;background:var(--brand)}
  .front-rule-thin{left:0;top:9px;width:100%;height:1px;background:var(--brand)}
  .headline-divider{left:249px;top:40px;width:2px;height:145px;background:#333}
  .headline{left:265px;top:36px;width:272px;font-family:"Roboto Condensed",sans-serif;line-height:1}
  .headline span{display:block;white-space:nowrap}
  .hl-light{font-weight:300;font-size:27px;letter-spacing:-.6px;color:var(--grey-text);margin-bottom:6px}
  .hl-blue{font-weight:400;font-size:31px;letter-spacing:-.3px;color:var(--brand-bright);margin-bottom:4px}
  .hl-small{font-weight:400;font-size:17px;letter-spacing:-.2px;color:var(--ink);margin-bottom:6px}
  .hl-blue-light{font-weight:300;font-size:27px;letter-spacing:-.6px;color:var(--brand-bright);margin-bottom:6px}
  .hl-bold{font-weight:700;font-size:31px;color:var(--ink)}
  .photo-band{left:0;top:255px;width:100%;height:272px;background:linear-gradient(180deg,#5563b4,#4654a8)}
  .values{left:0;top:532px;width:100%;height:178px;background:linear-gradient(180deg,#e6e6e8,#f4f4f5)}
  .value{position:absolute;top:0;width:176px;height:178px;text-align:center}
  .value__icon{position:absolute;left:50%;top:25px;margin-left:-28px;width:56px;height:56px;border-radius:50%;
    background:var(--dark);border:3px solid #fff;box-shadow:0 2px 5px rgba(0,0,0,.45);display:flex;align-items:center;justify-content:center}
  .value__label{position:absolute;left:0;right:0;top:114px;font-weight:900;font-size:14.5px;color:var(--brand)}
  .value-divider{top:12px;width:2px;height:118px;background:#444}

  .footer{left:0;width:100%;color:#fff;font-size:8.5px;line-height:1.25;display:flex}
  .footer--front{top:710px;height:72px;background:var(--dark)}
  .footer--back{top:713px;height:69px;background:var(--brand)}
  .footer__col{position:relative;padding:10px 0 0 36px;white-space:nowrap}
  .footer__col + .footer__col{padding-left:28px}
  .footer__col + .footer__col::before{content:"";position:absolute;left:0;top:12px;width:2px;height:44px;background:#fff}
  .footer__col svg{position:absolute;left:22px;top:11px}
  .footer__col + .footer__col svg{left:14px}
  .footer__col b{font-weight:700}

  /* back */
  .back-rule{left:0;top:0;width:100%;height:5px;background:#5a5a5c}
  .pitch-box{left:0;top:43px;width:272px;height:44px;background:var(--brand);color:#fff;
    font-family:"Roboto Condensed",sans-serif;font-weight:700;font-size:11.5px;line-height:1.4;padding:6px 0 0 22px;white-space:nowrap}
  .offer{left:284px;top:46px;width:262px}
  .offer__kicker{font-family:"Roboto Condensed",sans-serif;font-weight:300;font-size:12px;color:#444;white-space:nowrap;letter-spacing:-.5px}
  .offer__title{font-family:"Roboto Condensed",sans-serif;font-weight:700;font-size:29px;color:var(--brand);line-height:1.1;white-space:nowrap}
  .offer__text{font-size:11.5px;color:#333;line-height:1.3;margin-top:2px}
  .offer__value{font-weight:900;font-size:20px;color:var(--brand);letter-spacing:1px;margin-top:8px}
  .photo-grid{left:0;top:222px;width:100%;height:260px;background:#fff}
  .tile{position:absolute;background:linear-gradient(160deg,#6c8cbe,#2d4b7d)}
  .tile--warm{background:linear-gradient(160deg,#a6a9ae,#4a4e58)}
  .services-bg{left:0;top:482px;width:100%;height:231px;background:linear-gradient(180deg,#e4e4e6,#f3f3f4)}
  .service{position:absolute;background:var(--dark);color:#fff;text-align:center;font-size:17px;line-height:1.18}
  .service--raised{background:var(--dark-2);box-shadow:0 3px 10px rgba(0,0,0,.45);z-index:2}
  .service__icon{display:block;margin:0 auto}
</style>
</head>
<body>
<div class="canvas">

  <!-- FRONT: students -->
  <section class="flyer flyer--front" aria-label="Vorderseite für Studierende">
    <div class="abs front-rule"></div>
    <div class="abs front-rule-thin"></div>

    <div class="brand" style="left:32px;top:58px">
      <span class="brand__name">VENDA</span>
    </div>
    <div class="brand__sub abs" style="left:34px;top:104px">
      <b>Studentische Unternehmensberatung</b><br>Halvering Akademie für angewandte Studien
    </div>

    <div class="abs headline-divider"></div>
    <h1 class="abs headline">
      <span class="hl-light">WEG VON DEN BÜCHERN</span>
      <span class="hl-blue">RAN AN DIE PRAXIS</span>
      <span class="hl-small">Werde Teil eines dynamischen Teams</span>
      <span class="hl-blue-light">UND GESTALTE MIT UNS</span>
      <span class="hl-bold">DEINE ZUKUNFT</span>
    </h1>

    <div class="abs photo-band" role="img" aria-label="Blau getöntes Foto eines Seminarraums"></div>
    <svg class="abs" style="left:0;top:190px" width="558" height="330" viewBox="0 0 558 330">
      <circle cx="171" cy="162" r="158" fill="none" stroke="#2c2c30" stroke-width="2"/>
      <circle cx="399" cy="155" r="120" fill="none" stroke="#2c2c30" stroke-width="2"/>
      <circle cx="171" cy="162" r="146" fill="#fff"/>
      <circle cx="171" cy="162" r="140" fill="url(#g1)" role="img" aria-label="Foto: Studierende arbeiten gemeinsam am Tisch"/>
      <circle cx="399" cy="155" r="112" fill="#fff"/>
      <circle cx="399" cy="155" r="106" fill="url(#g2)" role="img" aria-label="Foto: Gruppe von Studierenden mit erhobenem Daumen"/>
      <defs>
        <linearGradient id="g1" x1="0" y1="0" x2="1" y2="1"><stop offset="0" stop-color="#d9d6cf"/><stop offset=".55" stop-color="#8a9bb8"/><stop offset="1" stop-color="#3f5b84"/></linearGradient>
        <linearGradient id="g2" x1="0" y1="0" x2="1" y2="1"><stop offset="0" stop-color="#ece6df"/><stop offset=".5" stop-color="#b69a86"/><stop offset="1" stop-color="#55607a"/></linearGradient>
      </defs>
    </svg>

    <div class="abs values">
      <div class="value" style="left:15px">
        <div class="value__icon"><svg width="28" height="28" viewBox="0 0 28 28" fill="none" stroke="#fff" stroke-width="1.6"><rect x="6" y="3" width="16" height="22" rx="1"/><path d="M10 12h8l-3-3M18 17h-8l3 3"/></svg></div>
        <div class="value__label">AUSTAUSCH</div>
      </div>
      <div class="abs value-divider" style="left:176px"></div>
      <div class="value" style="left:183px">
        <div class="value__icon"><svg width="30" height="28" viewBox="0 0 30 28" fill="none" stroke="#fff" stroke-width="1.5"><circle cx="10" cy="12" r="4"/><path d="M3 24c0-5 3-7 7-7s7 2 7 7"/><rect x="15" y="3" width="12" height="8" rx="1"/><path d="M18 6h6M18 8h4"/></svg></div>
        <div class="value__label">ERFAHRUNG</div>
      </div>
      <div class="abs value-divider" style="left:353px"></div>
      <div class="value" style="left:356px">
        <div class="value__icon"><svg width="30" height="28" viewBox="0 0 30 28" fill="#fff"><circle cx="15" cy="5" r="2.5"/><circle cx="6" cy="13" r="2"/><circle cx="12" cy="13" r="2"/><circle cx="18" cy="13" r="2"/><circle cx="24" cy="13" r="2"/><circle cx="6" cy="21" r="2"/><circle cx="12" cy="21" r="2"/><circle cx="18" cy="21" r="2"/><circle cx="24" cy="21" r="2"/><rect x="3" y="24" width="24" height="1.5"/></svg></div>
        <div class="value__label">GEMEINSCHAFT</div>
      </div>
    </div>

    <footer class="abs footer footer--front">
      <div class="footer__col" style="width:212px">
        <svg width="9" height="9" viewBox="0 0 10 10"><circle cx="5" cy="5" r="5" fill="#fff"/><circle cx="5" cy="4" r="1.6" fill="#3e3e40"/></svg>
        <b>VENDA Consulting e.V.</b><br>Studentische Unternehmensberatung<br>Brunnwieser Allee 37-41<br>26073 Oldenburg
      </div>
      <div class="footer__col" style="width:178px">
        <svg width="9" height="20" viewBox="0 0 10 22" fill="none" stroke="#fff" stroke-width="1.3"><rect x="1" y="2" width="8" height="6"/><path d="M1 2l4 3 4-3"/><circle cx="5" cy="16" r="4"/><path d="M1 16h8M5 12v8"/></svg>
        kontakt@venda-beratung.example<br>www.venda-beratung.example
      </div>
      <div class="footer__col" style="width:168px">
        <svg width="9" height="9" viewBox="0 0 10 10"><circle cx="5" cy="5" r="5" fill="#fff"/></svg>
        VENDA Consulting<br>e.V. Die studentische<br>Unternehmensberatung
      </div>
    </footer>
  </section>

  <!-- BACK: companies -->
  <section class="flyer flyer--back" aria-label="Rückseite für Unternehmen">
    <div class="abs back-rule"></div>
    <div class="abs pitch-box">Sie sind auf der Suche nach externer<br>Unterstützung für zielorientierte Problemlösungen?</div>

    <div class="abs offer">
      <div class="offer__kicker">WIR BIETEN IHREM UNTERNEHMEN EIN JUNGES UND</div>
      <div class="offer__title">DYNAMISCHES TEAM</div>
      <p class="offer__text">aus verschiedensten Fachrichtungen bei dem<br>nur eines im Fokus steht</p>
      <div class="offer__value">IHR MEHRWERT!</div>
    </div>

    <div class="brand" style="left:35px;top:120px">
      <span class="brand__name">VENDA</span>
    </div>
    <div class="brand__sub abs" style="left:37px;top:166px">
      <b>Studentische Unternehmensberatung</b><br>Halvering Akademie für angewandte Studien
    </div>

    <svg class="abs" style="left:0;top:188px" width="558" height="34"><polygon points="337,0 558,0 558,34 323,34" fill="var(--dark)"/></svg>

    <div class="abs photo-grid" role="img" aria-label="Bildraster: Geschäftsleute, Bürogebäude, Skyline, Handschlag, Laptop und Vertragsunterzeichnung">
      <div class="tile" style="left:0;top:0;width:130px;height:115px"></div>
      <div class="tile" style="left:137px;top:0;width:139px;height:115px"></div>
      <div class="tile tile--warm" style="left:283px;top:0;width:139px;height:115px"></div>
      <div class="tile tile--warm" style="left:429px;top:0;width:129px;height:115px"></div>
      <div class="tile" style="left:0;top:121px;width:130px;height:139px"></div>
      <div class="tile" style="left:137px;top:121px;width:139px;height:139px"></div>
      <div class="tile tile--warm" style="left:283px;top:121px;width:139px;height:139px"></div>
      <div class="tile" style="left:429px;top:121px;width:129px;height:139px"></div>
    </div>

    <div class="abs services-bg"></div>
    <svg class="abs" style="left:0;top:482px" width="558" height="34"><polygon points="0,0 237,0 225,34 0,34" fill="var(--dark)"/></svg>

    <div class="service" style="left:26px;top:550px;width:168px;height:110px;padding-top:18px">
      <svg class="service__icon" width="46" height="44" viewBox="0 0 46 44" fill="none" stroke="#bbb" stroke-width="1.2"><rect x="24" y="2" width="16" height="11"/><rect x="4" y="16" width="16" height="11"/><rect x="24" y="28" width="16" height="11"/><path d="M32 13v15M20 21h12"/></svg>
      <div style="margin-top:20px">Großes Netzwerk</div>
    </div>
    <div class="service service--raised" style="left:194px;top:543px;width:188px;height:123px;padding-top:24px">
      <svg class="service__icon" width="46" height="44" viewBox="0 0 46 44" fill="none" stroke="#ddd" stroke-width="1.3"><path d="M28 6a9 9 0 0 1 5 16v4h-10v-4a9 9 0 0 1 5-16z"/><path d="M24 29h8M25 32h6M12 40l9-10M9 36l6-6"/><path d="M28 1v2M38 4l-2 2M18 4l2 2M41 13h-2M15 13h2"/></svg>
      <div style="margin-top:26px">Frische Ideen</div>
    </div>
    <div class="service" style="left:382px;top:550px;width:148px;height:108px;padding-top:20px">
      <svg class="service__icon" width="34" height="34" viewBox="0 0 34 34" fill="none" stroke="#fff" stroke-width="1.2"><circle cx="17" cy="17" r="15"/><circle cx="17" cy="17" r="12"/><text x="17" y="22" text-anchor="middle" fill="#fff" stroke="none" font-family="Lato, sans-serif" font-size="12">24</text></svg>
      <div style="margin-top:10px">Flexible<br>Arbeitsweise</div>
    </div>

    <footer class="abs footer footer--back">
      <div class="footer__col" style="width:212px">
        <svg width="9" height="9" viewBox="0 0 10 10"><circle cx="5" cy="5" r="5" fill="#fff"/><circle cx="5" cy="4" r="1.6" fill="#3a4d98"/></svg>
        <b>VENDA Consulting e.V.</b><br>Studentische Unternehmensberatung<br>Brunnwieser Allee 37-41<br>26073 Oldenburg
      </div>
      <div class="footer__col" style="width:178px">
        <svg width="9" height="20" viewBox="0 0 10 22" fill="none" stroke="#fff" stroke-width="1.3"><rect x="1" y="2" width="8" height="6"/><path d="M1 2l4 3 4-3"/><circle cx="5" cy="16" r="4"/><path d="M1 16h8M5 12v8"/></svg>
        kontakt@venda-beratung.example<br>www.venda-beratung.example
      </div>
      <div class="footer__col" style="width:168px">
        <svg width="9" height="9" viewBox="0 0 10 10"><circle cx="5" cy="5" r="5" fill="#fff"/></svg>
        VENDA Consulting<br>e.V. Die studentische<br>Unternehmensberatung
      </div>
    </footer>
  </section>

</div>
</body>
</html>
```